PitchTally Webpages and Logo

See attached brief. Take the existing website www.pitchtally.co.uk and logo and transform these assets to:

Give people who arrive on the site for first time the confidence to sign-up easily and quickly
Allow regular returning users quick and easy placing of predictions and encourage them to share the PitchTally prediction on social networks and with their contacts
Convey the essence of a community working together to enjoyably come-up with smart predictions on sporting events
Work seamlessly and well across smartphones, tablets and desktop i.e. Should be Responsive Web Design
Updates

Target Market(s)

Users are sports fans with opinions
Primarily male and early twenties to mid-thirties
They are competitive - they want to beat their peers
Many are from outside the UK

Industry/Entity Type

Events

Logo Text

PitchTally

Coding

Coded - Design and coding required

Number of Pages Required

4 page

Font styles to use
Sans Serif

Requirements
Must have
• Responsive Web Design
• Mobile First
• HTML must work with dedicated bespoke application developed in ASP.NET using MS SQL underneath
• See Brief
Nice to have
• See brief
Should not have
• See brief

```html
<!DOCTYPE html>
<html lang="en">
<head>
<meta charset="utf-8">
<title>PitchTally – Altogether Better Predictions</title>
<link href="https://fonts.googleapis.com/css2?family=Bebas+Neue&family=PT+Sans:wght@400;700&family=Arimo:wght@400&display=swap" rel="stylesheet">
<style>
:root{
  --dark:#2e2e30;
  --teal:#27a795;
  --teal-dark:#1f8f80;
  --blue:#5aa9d6;
  --gold:#d9bd5c;
  --card:#f3f3f3;
  --text:#333;
  --muted:#555;
  --white:#fff;
  --link-blue:#3b5a9a;
  --chirp-blue:#55acee;
}
*{box-sizing:border-box;margin:0;padding:0}
html,body{width:770px;height:1200px;overflow:hidden;background:var(--white)}
body{font-family:"PT Sans",Arial,sans-serif;color:var(--text);position:relative}
.display{font-family:"Bebas Neue","Arial Narrow",sans-serif;font-weight:400}

/* Navigation */
.topbar{position:absolute;top:0;left:0;width:770px;height:42px;background:var(--dark);display:flex;align-items:center;padding:0 38px}
.brand{display:flex;align-items:center;gap:6px;color:var(--white);font-weight:700;font-size:13px;width:126px}
.brand-dot{width:12px;height:12px;border-radius:50%;background:var(--teal)}
.menu{display:flex;align-items:center;gap:0;font-size:9px;color:var(--white);font-weight:700;letter-spacing:.3px}
.menu a{color:inherit;text-decoration:none;padding:0 13px;height:21px;line-height:21px;border-radius:11px}
.menu a.active{background:var(--teal);padding:0 14px}
.signin{margin-left:auto;background:var(--blue);color:var(--white);font-size:9px;font-weight:700;height:21px;line-height:21px;padding:0 12px;border-radius:11px}
.search{margin-left:7px;width:94px;height:21px;border-radius:11px;background:#252527;color:#888;font-size:8.5px;line-height:21px;padding-left:20px;position:relative}
.search svg{position:absolute;left:8px;top:6px}

/* Hero */
.hero{position:absolute;top:42px;left:0;width:770px;height:385px;text-align:center;color:var(--white)}
.hero-photo{position:absolute;inset:0;background:radial-gradient(ellipse at 55% 40%,#6d7479 0%,#3e4347 45%,#1e2225 100%)}
.hero-content{position:relative}
.hero h1{font-size:38px;letter-spacing:1px;padding-top:32px;line-height:1}
.hero p.lead{font-size:14px;line-height:20px;width:450px;margin:17px auto 0}
.join{display:inline-block;margin-top:14px;background:var(--teal);color:var(--white);font-weight:700;font-size:11px;height:27px;line-height:27px;width:94px;border-radius:14px}
.features{position:absolute;top:236px;left:0;width:770px}
.feature{position:absolute;width:220px;margin-left:-110px}
.feature .icon{width:57px;height:57px;border-radius:50%;margin:0 auto;display:flex;align-items:center;justify-content:center}
.feature h2{font-size:26px;margin-top:8px;line-height:1}
.feature p{font-size:10.5px;line-height:13px;margin-top:4px}

/* Tips */
.tips-bar{position:absolute;top:450px;left:46px;width:676px;height:70px;border:1px solid #ececec;background:#fafafa;display:flex;align-items:center}
.tips-bar h2{font-size:23px;margin-left:16px;color:#333;letter-spacing:.3px;width:238px}
.share{position:absolute;top:23px;height:25px;width:172px;border-radius:3px;color:var(--white);font-family:Arial,sans-serif;font-weight:700;font-size:10px;display:flex;align-items:center}
.share .sq{width:24px;height:25px;display:flex;align-items:center;justify-content:center}
.share .sq span{width:9px;height:9px;background:var(--white);border-radius:1px;opacity:.85}
.share .label{flex:1;text-align:center}
.share.linkup{left:254px;background:var(--link-blue)}
.share.chirper{left:486px;background:var(--chirp-blue)}

.stats{position:absolute;top:539px;left:0;width:770px}
.stat{position:absolute;width:190px;margin-left:-95px;text-align:center}
.stat h3{font-size:19px;color:#333;margin-top:8px;line-height:1}
.stat .pct{font-size:28px;line-height:1;margin-top:6px}
.stat .cap{font-size:10px;line-height:12px;margin-top:5px;text-transform:uppercase;color:#333}
.divider{position:absolute;top:687px;left:0;width:770px;height:1px;background:#e6e6e6}

/* Match cards */
.card{position:absolute;width:213px;height:160px;background:var(--card);font-family:Arimo,Arial,sans-serif}
.teams{display:flex;justify-content:space-between;padding:11px 12px 0;font-size:10.5px;color:#444}
.versus{display:flex;align-items:center;justify-content:space-between;padding:0 17px;margin-top:8px}
.crest{width:50px;height:50px;border-radius:50%}
.crest.home{background:#c8333a}
.crest.away{background:#e4c24a}
.vs{font-size:24px;color:#555}
.date{text-align:center;font-size:8px;color:#444;margin-top:13px}
.predict{display:block;margin:6px auto 0;width:166px;height:24px;line-height:24px;background:var(--teal);color:var(--white);text-align:center;font-size:10px;border:1px solid var(--teal-dark)}
.kitty-text{position:absolute;left:24px;top:80px;font-size:12px;line-height:16px;color:#444;width:110px}
.kitty-photo{position:absolute;right:0;top:0;width:82px;height:160px;background:linear-gradient(160deg,#c89878 0%,#8a5e44 55%,#222 100%)}
.kitty-btn{position:absolute;left:24px;top:124px;width:166px;height:24px;background:var(--blue);color:var(--white);font-size:10px;line-height:24px;padding-left:38px;border:1px solid #4a95c0}
.kitty-btn svg{position:absolute;right:6px;top:4px}

/* Footer */
.footer{position:absolute;top:1086px;left:0;width:770px;height:114px;background:var(--dark);text-align:center;color:var(--white)}
.footer-links{display:flex;justify-content:center;gap:19px;font-size:9.5px;padding-top:23px}
.social{display:flex;justify-content:center;gap:11px;margin-top:19px}
.social span{width:21px;height:21px;border-radius:50%}
.copy{font-size:7.5px;color:#aaa;margin-top:13px}
</style>
</head>
<body>

<header class="topbar">
  <div class="brand"><span class="brand-dot"></span>PitchTally</div>
  <nav class="menu">
    <a class="active">HOME</a><a>MINILIGA</a><a>TABLES</a><a>KITTY</a><a>FAQ</a><a>ME</a>
  </nav>
  <div class="signin">Sign in ▾</div>
  <div class="search"><svg width="8" height="8" viewBox="0 0 8 8"><circle cx="3.3" cy="3.3" r="2.5" fill="none" stroke="#888" stroke-width="1"/><line x1="5.2" y1="5.2" x2="7.5" y2="7.5" stroke="#888" stroke-width="1"/></svg>Search</div>
</header>

<section class="hero">
  <div class="hero-photo" role="img" aria-label="Two footballers leaping for the ball under stadium lights"></div>
  <div class="hero-content">
    <h1 class="display">Altogether Better Predictions</h1>
    <p class="lead">Predict results, scores and scorers for your free chance to win a £20 Parcelo voucher every week. Overall season winner gets up to £1000 in Parcelo vouchers! No entry fee and no catches.</p>
    <span class="join">JOIN NOW</span>
  </div>
  <div class="features">
    <div class="feature" style="left:152px">
      <div class="icon" style="background:var(--teal)">
        <svg width="28" height="28" viewBox="0 0 28 28"><path d="M14 3a9 9 0 0 0-9 9c0 3 1.4 5 3 6.5V25h8v-3h3a2 2 0 0 0 2-2v-3h2l-2-5a9 9 0 0 0-7-9z" fill="#fff"/><circle cx="11" cy="11" r="1.2" fill="#27a795"/><circle cx="14" cy="11" r="1.2" fill="#27a795"/><circle cx="17" cy="11" r="1.2" fill="#27a795"/></svg>
      </div>
      <h2 class="display">Predict</h2>
      <p>The scores from the 5 matches this weekend</p>
    </div>
    <div class="feature" style="left:385px">
      <div class="icon" style="background:var(--blue)">
        <svg width="26" height="26" viewBox="0 0 26 26"><rect x="3" y="8" width="20" height="6" fill="#fff"/><rect x="5" y="14" width="16" height="9" fill="#fff"/><rect x="11.5" y="8" width="3" height="15" fill="#e05a4a"/><path d="M13 8c-2-4-6-4-6-1s4 1 6 1c2 0 6 2 6-1s-4-3-6 1z" fill="#e05a4a"/></svg>
      </div>
      <h2 class="display">Get Tips</h2>
      <p>Based on the wisdom of the crowd</p>
    </div>
    <div class="feature" style="left:616px">
      <div class="icon" style="background:var(--gold)">
        <svg width="26" height="26" viewBox="0 0 26 26"><path d="M7 4h12v5a6 6 0 0 1-12 0z" fill="#fff"/><path d="M7 6H3c0 4 2 6 4.5 6M19 6h4c0 4-2 6-4.5 6" fill="none" stroke="#fff" stroke-width="1.6"/><rect x="11.5" y="15" width="3" height="5" fill="#fff"/><rect x="8" y="20" width="10" height="3" fill="#fff"/></svg>
      </div>
      <h2 class="display">Enjoy</h2>
      <p>The glory of being a top tipster and scooping the jackpot!</p>
    </div>
  </div>
</section>

<section class="tips-bar">
  <h2 class="display">Tips from the crowd</h2>
  <div class="share linkup"><span class="sq"><span></span></span><span class="label">Share on Linkup</span></div>
  <div class="share chirper"><span class="sq"><span></span></span><span class="label">Share on Chirper</span></div>
</section>

<section class="stats">
  <div class="stat" style="left:152px">
    <svg width="34" height="36" viewBox="0 0 34 36"><path d="M5 0h9l5 10-6 4zM29 0h-9l-5 10 6 4z" fill="#27a795"/><circle cx="17" cy="23" r="12" fill="#e8c04a"/><circle cx="17" cy="23" r="9" fill="#f2d15e"/><path d="M17 16l2 4.3 4.6.5-3.4 3.1 1 4.6-4.2-2.4-4.2 2.4 1-4.6-3.4-3.1 4.6-.5z" fill="#d49a2a"/></svg>
    <h3 class="display">Result</h3>
    <div class="pct display" style="color:var(--teal)">100%</div>
    <div class="cap">Eastbrook United win</div>
  </div>
  <div class="stat" style="left:384px">
    <svg width="34" height="36" viewBox="0 0 34 36"><path d="M5 0h9l5 10-6 4zM29 0h-9l-5 10 6 4z" fill="#27a795"/><circle cx="17" cy="23" r="12" fill="#e8c04a"/><circle cx="17" cy="23" r="9" fill="#f2d15e"/><path d="M17 16l2 4.3 4.6.5-3.4 3.1 1 4.6-4.2-2.4-4.2 2.4 1-4.6-3.4-3.1 4.6-.5z" fill="#d49a2a"/></svg>
    <h3 class="display">Score</h3>
    <div class="pct display" style="color:var(--blue)">100%</div>
    <div class="cap">Ashton Vale 0 Irwell<br>United 2</div>
  </div>
  <div class="stat" style="left:618px">
    <svg width="34" height="36" viewBox="0 0 34 36"><path d="M5 0h9l5 10-6 4zM29 0h-9l-5 10 6 4z" fill="#27a795"/><circle cx="17" cy="23" r="12" fill="#e8c04a"/><circle cx="17" cy="23" r="9" fill="#f2d15e"/><path d="M17 16l2 4.3 4.6.5-3.4 3.1 1 4.6-4.2-2.4-4.2 2.4 1-4.6-3.4-3.1 4.6-.5z" fill="#d49a2a"/></svg>
    <h3 class="display">1st Goal</h3>
    <div class="pct display" style="color:var(--gold)">57%</div>
    <div class="cap">Durant C</div>
  </div>
</section>

<div class="divider"></div>

<section class="matches">
  <article class="card" style="left:46px;top:717px">
    <div class="teams"><span>Merseyvale FC</span><span>Royal Meseta</span></div>
    <div class="versus"><span class="crest home"></span><span class="vs">VS</span><span class="crest away"></span></div>
    <div class="date">14 October 2013, 23:00 (FT)</div>
    <span class="predict">PREDICT SCORE NOW</span>
  </article>
  <article class="card" style="left:278px;top:717px">
    <div class="teams"><span>Merseyvale FC</span><span>Royal Meseta</span></div>
    <div class="versus"><span class="crest home"></span><span class="vs">VS</span><span class="crest away"></span></div>
    <div class="date">14 October 2013, 23:00 (FT)</div>
    <span class="predict">PREDICT SCORE NOW</span>
  </article>
  <article class="card" style="left:509px;top:717px">
    <div class="teams"><span>Merseyvale FC</span><span>Royal Meseta</span></div>
    <div class="versus"><span class="crest home"></span><span class="vs">VS</span><span class="crest away"></span></div>
    <div class="date">14 October 2013, 23:00 (FT)</div>
    <span class="predict">PREDICT SCORE NOW</span>
  </article>
  <article class="card" style="left:46px;top:896px">
    <div class="teams"><span>Merseyvale FC</span><span>Royal Meseta</span></div>
    <div class="versus"><span class="crest home"></span><span class="vs">VS</span><span class="crest away"></span></div>
    <div class="date">14 October 2013, 23:00 (FT)</div>
    <span class="predict">PREDICT SCORE NOW</span>
  </article>
  <article class="card" style="left:278px;top:896px">
    <div class="teams"><span>Merseyvale FC</span><span>Royal Meseta</span></div>
    <div class="versus"><span class="crest home"></span><span class="vs">VS</span><span class="crest away"></span></div>
    <div class="date">14 October 2013, 23:00 (FT)</div>
    <span class="predict">PREDICT SCORE NOW</span>
  </article>
  <article class="card kitty" style="left:509px;top:896px">
    <div class="kitty-photo" role="img" aria-label="Smiling top tipster of the week"></div>
    <p class="kitty-text">See how Mr Kestel got on last week</p>
    <span class="kitty-btn">SEE THE KITTY (30)
      <svg width="15" height="15" viewBox="0 0 15 15"><circle cx="7.5" cy="7.5" r="6.5" fill="none" stroke="#fff" stroke-width="1"/><path d="M4.5 9l3-3 3 3" fill="none" stroke="#fff" stroke-width="1.2"/></svg>
    </span>
  </article>
</section>

<footer class="footer">
  <nav class="footer-links"><span>About</span><span>Terms</span><span>Site Map</span><span>Privacy</span><span>Contact Us</span></nav>
  <div class="social">
    <span style="background:#3b5a9a"></span>
    <span style="background:#3ba9e0"></span>
    <span style="background:#e84c8b"></span>
    <span style="background:#44a8c8"></span>
    <span style="background:#e0574a"></span>
  </div>
  <p class="copy">© PitchTally 2014 – All Right Reserved</p>
</footer>

</body>
</html>
```